Building company buisness cards

We are looking for a sharp modern new look for our business cards.
We are a New Zealand based company that specialises in house and land packages.
We have attached a photo of the current logo and would like to see if it can be improved somehow if needed.
We are open to any colours but we have chosen green at this stage.
Feel free to change the font and make the logo smarter looking.
Play with the colours and see what looks best.

We want a card that looks so good know one will want to throw it away!

Target Market(s)

Home buyers

Industry/Entity Type

Building

Contact Information for Business Card

Dorian Keswick
0217392604
dkeswick@tidewellhomecraft.co.nz
tidewellhomecraft.co.nz

Font styles to use
Serif
Sans Serif

Colors

Designer to choose colors to be used in the design.

Requirements
Must have
• Logo and company name on one side, details on the other side
Nice to have
• Color codes for the original green are HEX #4a8028, RGB(74,128,40), CMYK(42,0,69,50)
• Round corners, Raised and/or spot UV

```html
<!DOCTYPE html>
<html lang="en">
<head>
<meta charset="utf-8">
<title>Tidewell Homecraft – Business Cards</title>
<link rel="stylesheet" href="https://fonts.googleapis.com/css2?family=Montserrat:wght@700;800&family=Open+Sans:wght@400&display=swap">
<style>
  :root {
    --brand-green: #66913f;
    --brand-green-dark: #4a8028;
    --brand-green-deep: #3f6e22;
    --brand-green-light: #7aa653;
    --brand-green-pale: #8fb86a;
    --card-white: #fbfbfb;
    --ink-grey: #3f3f3f;
    --muted-grey: #6a6a6a;
    --wordmark-grey: #7b7b7b;
    --page-bg: #ecebe8;
  }
  * { margin: 0; padding: 0; box-sizing: border-box; }
  html, body {
    width: 1200px; height: 1021px; overflow: hidden;
    background: var(--page-bg);
  }
  .canvas { position: relative; width: 1200px; height: 1021px; }

  .card {
    position: absolute;
    width: 560px; height: 320px;
    border-radius: 22px;
    overflow: hidden;
    box-shadow: 0 14px 30px rgba(0,0,0,.18);
  }

  /* Back: brand side */
  .card-back {
    left: 590px; top: 110px;
    background: var(--brand-green);
  }
  .card-back .pattern-area {
    position: absolute; inset: 0;
    background:
      radial-gradient(ellipse at 50% 50%, rgba(255,255,255,.10) 0%, rgba(255,255,255,0) 45%),
      repeating-linear-gradient(155deg, rgba(255,255,255,.07) 0 26px, rgba(0,0,0,.06) 26px 52px),
      linear-gradient(135deg, var(--brand-green-light) 0%, var(--brand-green) 55%, var(--brand-green-deep) 100%);
  }
  .card-back .wordmark {
    position: absolute; left: 0; right: 0; top: 132px;
    text-align: center;
    font-family: 'Montserrat', sans-serif;
    font-weight: 800;
    color: #ffffff;
    line-height: 1;
  }
  .card-back .wordmark-main { display: block; font-size: 40px; letter-spacing: .3px; }
  .card-back .wordmark-sub { display: block; font-size: 21px; margin-top: 4px; }

  /* Front: details side */
  .card-front {
    left: 60px; top: 520px;
    background: var(--card-white);
  }
  .card-front .accent-band {
    position: absolute; top: 0; right: 0; bottom: 0;
    width: 205px;
    background: var(--brand-green);
  }
  .card-front .illustration-area {
    position: absolute; left: 330px; top: 95px;
    width: 205px; height: 205px;
    border-radius: 12px;
    background: linear-gradient(160deg, var(--brand-green-pale) 0%, var(--brand-green-light) 60%, var(--brand-green) 100%);
  }
  .card-front .wordmark {
    position: absolute; left: 38px; top: 34px;
    font-family: 'Montserrat', sans-serif;
    font-weight: 800;
    line-height: 1;
  }
  .card-front .wordmark-main { display: block; font-size: 44px; color: var(--brand-green); }
  .card-front .wordmark-sub { display: block; font-size: 24px; color: var(--wordmark-grey); margin-top: 2px; }

  .contact-block {
    position: absolute; left: 38px; top: 150px;
    font-family: 'Open Sans', sans-serif;
  }
  .person-name {
    font-family: 'Montserrat', sans-serif;
    font-weight: 700;
    font-size: 21px;
    color: var(--brand-green);
  }
  .person-role {
    font-size: 14px;
    color: var(--muted-grey);
    margin-bottom: 18px;
  }
  .contact-line {
    display: flex; align-items: center; gap: 7px;
    font-size: 14.5px;
    color: var(--ink-grey);
    line-height: 22px;
  }
  .contact-line svg { width: 13px; height: 13px; flex: none; }
</style>
</head>
<body>
<main class="canvas">

  <section class="card card-back" aria-label="Card back">
    <div class="pattern-area" role="img" aria-label="Repeating embossed house-and-family pattern in green tones"></div>
    <div class="wordmark">
      <span class="wordmark-main">tidewell</span>
      <span class="wordmark-sub">homecraft.</span>
    </div>
  </section>

  <section class="card card-front" aria-label="Card front">
    <div class="accent-band"></div>
    <div class="illustration-area" role="img" aria-label="Large white house-and-family illustration on the green panel"></div>
    <div class="wordmark">
      <span class="wordmark-main">tidewell</span>
      <span class="wordmark-sub">homecraft.</span>
    </div>
    <div class="contact-block">
      <div class="person-name">Dorian Keswick</div>
      <div class="person-role">Founder</div>
      <div class="contact-line">
        <svg viewBox="0 0 16 16" aria-hidden="true"><path fill="var(--brand-green)" d="M3.6 1.2l2.3 2.6-1.2 1.8c.9 2 2.5 3.6 4.5 4.6l1.8-1.2 2.6 2.3-1.3 2.3C7 13.2 2.8 9 1.4 3z"/></svg>
        <span>0217392604</span>
      </div>
      <div class="contact-line">
        <svg viewBox="0 0 16 16" aria-hidden="true"><rect x="1.5" y="3.5" width="13" height="9" fill="none" stroke="var(--brand-green)" stroke-width="1.6"/><path d="M1.5 3.5L8 9l6.5-5.5" fill="none" stroke="var(--brand-green)" stroke-width="1.6"/></svg>
        <span>dkeswick@tidewellhomecraft.co.nz</span>
      </div>
      <div class="contact-line">
        <svg viewBox="0 0 16 16" aria-hidden="true"><circle cx="8" cy="8" r="6.5" fill="none" stroke="var(--brand-green)" stroke-width="1.4"/><ellipse cx="8" cy="8" rx="2.8" ry="6.5" fill="none" stroke="var(--brand-green)" stroke-width="1.2"/><path d="M1.5 8h13" stroke="var(--brand-green)" stroke-width="1.2"/></svg>
        <span>tidewellhomecraft.co.nz</span>
      </div>
    </div>
  </section>

</main>
</body>
</html>
```